Talvick Industrial Maintenance Business Card

Design a business card with the following information, logo must be included.
Talvick Industrial Maintenance
Dan Pelfrey Jr.
Pone 555-214-7608
email dan.pelfrey.jr@mailvantor.com

```html
<!DOCTYPE html>
<html lang="en">
<head>
<meta charset="utf-8">
<title>Talvick Industrial Maintenance – Business Card</title>
<link href="https://fonts.googleapis.com/css2?family=Montserrat:wght@400;500;700&display=swap" rel="stylesheet">
<style>
  :root {
    --brand-blue: #0a74bf;
    --paper: #f7f7f7;
    --ink-grey: #555555;
    --rule-grey: #b5b5b5;
    --backdrop: #e2e2e2;
  }
  * { box-sizing: border-box; margin: 0; padding: 0; }
  html, body {
    width: 1200px;
    height: 930px;
    overflow: hidden;
    background: var(--backdrop);
    font-family: "Montserrat", Arial, sans-serif;
  }
  .canvas {
    position: relative;
    width: 1200px;
    height: 930px;
  }
  .card {
    position: absolute;
    top: 316px;
    width: 520px;
    height: 297px;
    box-shadow: 0 6px 18px rgba(0,0,0,0.12);
  }
  .card--front { left: 50px; background: var(--paper); }
  .card--back  { left: 630px; background: var(--brand-blue); }

  .brand {
    position: absolute;
    display: flex;
    align-items: center;
    gap: 14px;
  }
  .brand__dot {
    width: 46px;
    height: 46px;
    border-radius: 50%;
    flex: none;
  }
  .brand__name {
    font-weight: 700;
    line-height: 1.05;
    text-transform: uppercase;
  }
  .brand__name .big { display: block; font-size: 36px; letter-spacing: 1px; }
  .brand__name .small { display: block; font-size: 11.5px; letter-spacing: 1.6px; }

  .card--front .brand { left: 70px; top: 56px; }
  .card--front .brand__dot { background: var(--brand-blue); }
  .card--front .brand__name { color: var(--brand-blue); }

  .card--back .brand { left: 50%; top: 50%; transform: translate(-50%, -50%); }
  .card--back .brand__dot { background: #ffffff; }
  .card--back .brand__name { color: #ffffff; }

  .contact {
    position: absolute;
    left: 70px;
    top: 160px;
  }
  .contact__name {
    color: var(--brand-blue);
    font-weight: 700;
    font-size: 17px;
    letter-spacing: 1px;
    text-transform: uppercase;
  }
  .contact__rule {
    width: 150px;
    height: 1px;
    background: var(--rule-grey);
    margin: 8px 0 9px;
  }
  .contact__line {
    color: var(--ink-grey);
    font-size: 12.5px;
    letter-spacing: 0.8px;
    text-transform: uppercase;
    line-height: 1.7;
  }
  .contact__label { color: var(--brand-blue); font-weight: 500; }
</style>
</head>
<body>
<main class="canvas">
  <section class="card card--front">
    <div class="brand">
      <span class="brand__dot"></span>
      <span class="brand__name">
        <span class="big">Talvick</span>
        <span class="small">Industrial Maintenance</span>
      </span>
    </div>
    <div class="contact">
      <p class="contact__name">Dan Pelfrey Jr.</p>
      <div class="contact__rule"></div>
      <p class="contact__line"><span class="contact__label">P:</span> 555-214-7608</p>
      <p class="contact__line"><span class="contact__label">E:</span> dan.pelfrey.jr@mailvantor.com</p>
    </div>
  </section>

  <section class="card card--back">
    <div class="brand">
      <span class="brand__dot"></span>
      <span class="brand__name">
        <span class="big">Talvick</span>
        <span class="small">Industrial Maintenance</span>
      </span>
    </div>
  </section>
</main>
</body>
</html>
```